KR Stationary Design

Logo, Business Card, Letterhead & Email Signature Design

Target Market(s)

Legal

Colors

Designer to choose colors to be used in the design.

Requirements
Must have
• Gold and Blue are the colours to use. The KR must be inside the Gold Legal Pendulum

```html
<!DOCTYPE html>
<html lang="en">
<head>
<meta charset="utf-8">
<title>KR Stationery – Ravenhall Incorporated</title>
<link href="https://fonts.googleapis.com/css2?family=Montserrat:wght@400;500;600;700&display=swap" rel="stylesheet">
<style>
  :root{
    --bg:#dcdcdc;
    --ink:#1b1b1b;
    --paper:#f6f6f6;
    --gold:#c19a3a;
    --blue:#2a45b0;
    --blue-deep:#1c2e7a;
    --text-dark:#2a2a2a;
    --text-light:#e4e4e4;
    --watermark:#e7e7ec;
  }
  *{box-sizing:border-box;margin:0;padding:0}
  html,body{width:1200px;height:900px;overflow:hidden}
  body{background:var(--bg);font-family:"Montserrat",sans-serif;position:relative}
  .piece{position:absolute;box-shadow:0 3px 8px rgba(0,0,0,.25)}
  .dark{background:var(--ink)}

  /* brand lockup: name in one colour, one weight, with a plain circle */
  .brand{display:flex;align-items:center;gap:calc(var(--s)*.35);white-space:nowrap;line-height:1}
  .brand-mark{width:calc(var(--s)*.8);height:calc(var(--s)*.8);border-radius:50%;background:var(--gold);flex:none}
  .brand-name{color:var(--gold);font-weight:500;font-size:var(--s);letter-spacing:.02em}

  .site-line{position:absolute;color:var(--blue);font-size:4px;letter-spacing:.08em;white-space:nowrap}

  /* business cards */
  .card-front{left:311px;top:88px;width:114px;height:64px;display:flex;align-items:center;justify-content:center}
  .card-back{left:311px;top:163px;width:114px;height:64px}
  .card-back .brand{position:absolute;right:3px;top:10px}
  .card-name{position:absolute;left:3px;top:30px;color:var(--gold);font-size:4.6px;font-weight:500;white-space:nowrap}
  .card-role{position:absolute;left:3px;top:36px;color:var(--text-light);font-size:3px;white-space:nowrap}
  .card-contacts{position:absolute;left:3px;bottom:4px;color:var(--text-light);font-size:2.8px;line-height:1.5;list-style:none;white-space:nowrap}
  .card-contacts li::before{content:"";display:inline-block;width:2px;height:2px;background:var(--gold);margin-right:2px;vertical-align:middle}
  .card-address{position:absolute;right:3px;bottom:4px;color:var(--text-light);font-size:2.8px;line-height:1.5;text-align:right;white-space:nowrap}

  .badge{left:223px;top:169px;width:54px;height:54px;border-radius:50%;background:#fbfbfb;display:flex;align-items:center;justify-content:center}

  /* envelopes */
  .envelope-large{left:225px;top:247px;width:203px;height:288px}
  .envelope-large .brand{position:absolute;right:11px;bottom:44px}
  .envelope-large .site-line{left:11px;bottom:18px}
  .envelope-dl{left:165px;top:566px;width:264px;height:124px}
  .envelope-dl .brand{position:absolute;right:9px;bottom:18px}
  .envelope-dl .site-line{left:10px;bottom:8px}
  .envelope-square{left:763px;top:567px;width:157px;height:157px;display:flex;align-items:center;justify-content:center}
  .envelope-square .site-line{bottom:14px;left:0;right:0;text-align:center}
  .flap{position:absolute;left:0;top:0;width:100%;height:100%;pointer-events:none}

  /* letterhead */
  .letterhead{left:463px;top:164px;width:264px;height:373px;background:var(--paper)}
  .letterhead .brand{position:absolute;left:10px;top:30px}
  .lh-contacts{position:absolute;right:14px;top:34px;list-style:none;text-align:right;color:var(--text-dark);font-size:4.6px;line-height:1.4;white-space:nowrap}
  .lh-contacts li::after{content:"";display:inline-block;width:2.5px;height:2.5px;border-radius:50%;background:var(--blue);margin-left:3px;vertical-align:middle}
  .lh-watermark{position:absolute;left:0;right:0;top:178px;text-align:center;color:var(--watermark);font-weight:500;font-size:30px;white-space:nowrap}
  .lh-address{position:absolute;left:0;right:0;bottom:12px;text-align:center;color:var(--text-dark);font-size:4.8px;white-space:nowrap}
  .lh-address svg{display:block;margin:0 auto 2px}
  .lh-band{position:absolute;left:0;right:0;bottom:0;height:6px;background:linear-gradient(90deg,var(--blue),var(--blue-deep))}

  /* presentation folder */
  .folder{left:760px;top:154px;width:271px;height:384px;background:linear-gradient(180deg,var(--ink) 0%,var(--ink) 45%,#2e2e2e 100%)}
  .folder .brand{position:absolute;left:0;right:0;top:118px;justify-content:center}

  /* notebook */
  .notebook{left:547px;top:565px;width:182px;height:265px;border-radius:0 9px 9px 0;background:linear-gradient(180deg,var(--ink) 0%,var(--ink) 55%,#2b2b2b 100%)}
  .notebook .brand{position:absolute;left:0;right:26px;top:84px;justify-content:center}
  .notebook-strap{position:absolute;right:34px;top:0;width:6px;height:100%;background:#0d1330}
  .notebook-ribbon{position:absolute;left:12px;top:265px;width:4px;height:46px;background:#8a1c6e}

  /* email signature */
  .signature{left:165px;top:725px;width:262px;height:60px;border-bottom:1.5px solid var(--blue)}
  .sig-photo{position:absolute;left:8px;top:7px;width:45px;height:45px;border-radius:50%;border:2px solid var(--blue);background:radial-gradient(circle at 50% 40%,#b9c2cf,#3b4d72)}
  .sig-name{position:absolute;left:60px;top:14px;color:var(--blue);font-weight:700;font-size:7px;text-transform:uppercase;white-space:nowrap}
  .sig-role{position:absolute;left:60px;top:24px;color:var(--text-light);font-size:4.4px;line-height:1.6;white-space:nowrap}
  .sig-contacts{position:absolute;left:155px;top:13px;list-style:none;color:var(--text-light);font-size:6px;line-height:1.4;white-space:nowrap}
  .sig-contacts li::before{content:"";display:inline-block;width:2.5px;height:2.5px;background:var(--blue);margin-right:3px;vertical-align:middle}
  .sig-follow{position:absolute;left:155px;top:46px;color:var(--blue);font-size:6px;font-weight:600;display:flex;align-items:center;gap:4px;white-space:nowrap}
  .sig-follow span.dot{width:7px;height:7px;border-radius:50%;background:var(--blue);display:inline-block}
</style>
</head>
<body>

  <div class="piece dark card-front">
    <div class="brand" style="--s:7px"><span class="brand-mark"></span><span class="brand-name">KR Ravenhall</span></div>
  </div>

  <div class="piece dark card-back">
    <div class="brand" style="--s:4.5px"><span class="brand-mark"></span><span class="brand-name">KR Ravenhall</span></div>
    <p class="card-name">DYLAN MARSH</p>
    <p class="card-role">Founder &amp; CEO</p>
    <ul class="card-contacts">
      <li>02 5550 3921</li>
      <li>hello@ravenhall.law</li>
      <li>www.ravenhall.law</li>
    </ul>
    <p class="card-address">PO Box 3190<br>Ashgrove NSW 2150</p>
  </div>

  <div class="piece badge">
    <div class="brand" style="--s:4.5px"><span class="brand-mark"></span><span class="brand-name">KR Ravenhall</span></div>
  </div>

  <div class="piece dark envelope-large">
    <svg class="flap" viewBox="0 0 203 288" preserveAspectRatio="none"><path d="M0 0 L10 25 H193 L203 0" fill="none" stroke="#262626" stroke-width="1"/></svg>
    <div class="brand" style="--s:11px"><span class="brand-mark"></span><span class="brand-name">KR Ravenhall</span></div>
    <p class="site-line">www.ravenhall.law</p>
  </div>

  <div class="piece letterhead">
    <div class="brand" style="--s:6.5px"><span class="brand-mark"></span><span class="brand-name">KR Ravenhall</span></div>
    <ul class="lh-contacts">
      <li>021 555 0148</li>
      <li>hello@ravenhall.law</li>
      <li>www.ravenhall.law</li>
    </ul>
    <p class="lh-watermark" aria-hidden="true">KR Ravenhall</p>
    <p class="lh-address">
      <svg width="4" height="5" viewBox="0 0 8 10"><path d="M4 0a3 3 0 0 1 3 3c0 2.5-3 6-3 6S1 5.5 1 3a3 3 0 0 1 3-3z" fill="var(--blue)"/></svg>
      Harbour House Elm Court, Dunmore, DK4 2LP
    </p>
    <div class="lh-band"></div>
  </div>

  <div class="piece folder">
    <div class="brand" style="--s:20px"><span class="brand-mark"></span><span class="brand-name">KR Ravenhall</span></div>
  </div>

  <div class="piece dark envelope-dl">
    <div class="brand" style="--s:7.5px"><span class="brand-mark"></span><span class="brand-name">KR Ravenhall</span></div>
    <p class="site-line">www.ravenhall.law</p>
  </div>

  <div class="piece dark signature">
    <div class="sig-photo" role="img" aria-label="Portrait photo of Nathan Cole"></div>
    <p class="sig-name">Nathan Cole</p>
    <p class="sig-role">Director / Structural Engineer<br>BEng(Hons) CPEng CMengNZ IntPE(NZ)</p>
    <ul class="sig-contacts">
      <li>021 555 0148</li>
      <li>hello@ravenhall.law</li>
      <li>www.ravenhall.law</li>
    </ul>
    <p class="sig-follow">Follow Me on: <span class="dot"></span><span class="dot"></span><span class="dot"></span><span class="dot"></span></p>
  </div>

  <div class="piece notebook">
    <div class="brand" style="--s:10px"><span class="brand-mark"></span><span class="brand-name">KR Ravenhall</span></div>
    <div class="notebook-strap"></div>
    <div class="notebook-ribbon"></div>
  </div>

  <div class="piece dark envelope-square">
    <svg class="flap" viewBox="0 0 157 157" preserveAspectRatio="none"><path d="M8 0 L20 28 H157" fill="none" stroke="#262626" stroke-width="1"/></svg>
    <div class="brand" style="--s:9px"><span class="brand-mark"></span><span class="brand-name">KR Ravenhall</span></div>
    <p class="site-line">www.ravenhall.law</p>
  </div>

</body>
</html>
```